New logo + business card design

Need a new logo and business card design. Business is a management consultancy specialising in governance and board advisory. Want a modern, contemporary but professional feel to the logo and business card. Also need all the information within the current business card on the new one including ABN which is: 58 204 936 417. Also my title is Principal not Director. Need 2 versions of the logo - one with the tagline, one without and of course in all the relevant formats. png, for black background etc.
Also need to be provided with native formats for updates in the future to the business card.

Target Market(s)

Board and executive management in large listed organisations.

Industry/Entity Type

Professional Service

Font styles to use
Sans Serif

Colors
3276b5
0255a3
85acd3

Requirements
Must have
• includes typefaces that are already on standard word and pdf so easy for others to view. Must be limited to a maximum of 2 colours (preferably one) excluding the typeface/font colour for economical printing. prefer silhouette type logo's not detailed ones.
Nice to have
• prefer rounder looking typefaces e.g century gothic versus arial.
Should not have
• do not want anything too legal looking

```html
<!DOCTYPE html>
<html lang="en">
<head>
<meta charset="utf-8">
<title>Arden Advisory – Business Card</title>
<link rel="stylesheet" href="https://fonts.googleapis.com/css2?family=Arimo:wght@400;700&display=swap">
<style>
  :root {
    --page-bg: #ececec;
    --card-blue: #0a55a8;
    --card-blue-deep: #034a97;
    --icon-blue: #2f75bc;
    --text-white: #ffffff;
    --text-soft: #e6eef8;
  }
  * { box-sizing: border-box; margin: 0; padding: 0; }
  html, body { width: 1200px; height: 900px; overflow: hidden; }
  body {
    background: var(--page-bg);
    font-family: "Arimo", Arial, sans-serif;
    position: relative;
  }
  .business-card {
    position: absolute;
    left: 120px; top: 176px;
    width: 960px; height: 548px;
    background: radial-gradient(ellipse at 40% 45%, var(--card-blue) 0%, var(--card-blue-deep) 100%);
    color: var(--text-white);
    box-shadow: 0 6px 18px rgba(0,0,0,0.18);
  }
  .brand-block {
    position: absolute;
    left: 0; width: 382px; top: 304px;
    text-align: center;
  }
  .brand-name {
    font-size: 27px;
    font-weight: 400;
    letter-spacing: 0.5px;
    line-height: 1;
  }
  .brand-tagline {
    margin-top: 9px;
    font-size: 8.5px;
    font-weight: 700;
    letter-spacing: 0.6px;
    line-height: 1;
  }
  .abn {
    margin-top: 38px;
    font-size: 26px;
    line-height: 1;
  }
  .person {
    position: absolute;
    left: 384px; top: 62px;
  }
  .person-name { font-size: 44px; font-weight: 700; line-height: 1; }
  .person-title { font-size: 24px; margin-top: 12px; line-height: 1; color: var(--text-soft); }
  .contact-list { list-style: none; }
  .contact-item {
    position: absolute;
    left: 381px;
    display: flex;
    align-items: flex-start;
    font-size: 26px;
    line-height: 36px;
  }
  .contact-icon {
    flex: none;
    width: 44px; height: 44px;
    border-radius: 50%;
    background: var(--icon-blue);
    display: flex; align-items: center; justify-content: center;
    margin-right: 22px;
    margin-top: -4px;
  }
  .contact-icon svg { width: 22px; height: 22px; }
  .icon-solid { fill: var(--text-white); }
  .icon-line { fill: none; stroke: var(--text-white); }
  .contact-phone { top: 236px; }
  .contact-email { top: 302px; }
  .contact-address { top: 375px; }
  .contact-web { top: 472px; }
</style>
</head>
<body>
  <article class="business-card">
    <div class="brand-block">
      <p class="brand-name">ARDEN ADVISORY</p>
      <p class="brand-tagline">CLEAR COUNSEL FOR BOARDS AND EXECUTIVES</p>
      <p class="abn">ABN: 58 204 936 417</p>
    </div>

    <header class="person">
      <h1 class="person-name">Clara Whitmore</h1>
      <p class="person-title">PRINCIPAL</p>
    </header>

    <ul class="contact-list">
      <li class="contact-item contact-phone">
        <span class="contact-icon">
          <svg class="icon-solid" viewBox="0 0 24 24"><path d="M6.6 10.8a15.1 15.1 0 0 0 6.6 6.6l2.2-2.2c.3-.3.7-.4 1-.2 1.1.4 2.3.6 3.6.6.6 0 1 .4 1 1V20c0 .6-.4 1-1 1A17 17 0 0 1 3 4c0-.6.4-1 1-1h3.5c.6 0 1 .4 1 1 0 1.3.2 2.5.6 3.6.1.3 0 .7-.2 1z"/></svg>
        </span>
        <span>0412 580 316</span>
      </li>
      <li class="contact-item contact-email">
        <span class="contact-icon">
          <svg class="icon-line" viewBox="0 0 24 24" stroke-width="2"><path d="M3 6h18v12H3z"/><path d="M3 6l9 7 9-7"/></svg>
        </span>
        <span>clarew@ardenadvisory.com.au</span>
      </li>
      <li class="contact-item contact-address">
        <span class="contact-icon">
          <svg class="icon-solid" viewBox="0 0 24 24"><path d="M12 2a7 7 0 0 0-7 7c0 5.2 7 13 7 13s7-7.8 7-13a7 7 0 0 0-7-7zm0 9.5a2.5 2.5 0 1 1 0-5 2.5 2.5 0 0 1 0 5z"/></svg>
        </span>
        <span>Level 4/58 Harbour Rd, Surry Hills,<br>NSW 2010, Sydney, AUSTRALIA</span>
      </li>
      <li class="contact-item contact-web">
        <span class="contact-icon">
          <svg class="icon-line" viewBox="0 0 24 24" stroke-width="1.6"><circle cx="12" cy="12" r="9"/><ellipse cx="12" cy="12" rx="4" ry="9"/><path d="M3 12h18M4.5 7.5h15M4.5 16.5h15"/></svg>
        </span>
        <span>www.ardenadvisory.com.au</span>
      </li>
    </ul>
  </article>
</body>
</html>
```